Labels for probiotic care products as Body Cream, Shower gel, Hand soap, ....

We are a starting a business in Flanders Belgium. We are looking for a label for care products, based on probiotics or good bacterie. We are looking for a fresh design that attracts people who wants a good product, based on naturally components. The products make that the microflora of the skin becomes and remains natural. The label must we be adaptive on bottles of 15 cm height to 8 cm height and a width of 4,5 cm. The brand name is KOLA EMU (beautiful skin in Hawaiian) or maybe just KOLA.

Industry/Entity Type

Business

Colors

Designer to choose colors to be used in the design.

Requirements
Must have
• somewhere the text "Probiotic Skin Care"
• I also have to tell that the bottles are white.
Nice to have
• I uploaded the 9 existing labels, but I want a totally new one, because the labels of our cleaning products are the same. I also uploaded a mood bord of labels I like.

```html
<!DOCTYPE html>
<html lang="en">
<head>
<meta charset="utf-8">
<title>KOLA EMU – Skin Repair Label</title>
<link href="https://fonts.googleapis.com/css2?family=Josefin+Sans:wght@300&family=Roboto+Slab:wght@600&display=swap" rel="stylesheet">
<style>
  :root {
    --backdrop: #ececec;
    --label-white: #ffffff;
    --pattern-light: #f4f5f8;
    --pattern-mid: #dfe2ea;
    --panel-navy: #232f48;
    --panel-text: #ffffff;
    --accent-orange: #f0642a;
  }
  html, body {
    margin: 0;
    padding: 0;
    width: 1175px;
    height: 1200px;
    overflow: hidden;
    background: var(--backdrop);
  }
  .canvas {
    position: relative;
    width: 1175px;
    height: 1200px;
  }
  .label {
    position: absolute;
    left: 411px;
    top: 100px;
    width: 352px;
    height: 1000px;
    background: var(--label-white);
  }
  .label__pattern {
    position: absolute;
    inset: 0;
    background: linear-gradient(135deg, var(--pattern-light), var(--pattern-mid) 50%, var(--pattern-light));
  }
  .brand-panel {
    position: absolute;
    left: 48px;
    top: 243px;
    width: 256px;
    height: 397px;
    background: var(--panel-navy);
    color: var(--panel-text);
    text-align: center;
    overflow: hidden;
  }
  .brand-panel__frame {
    position: absolute;
    inset: 7px;
    border: 1px solid rgba(255, 255, 255, 0.75);
  }
  .brand-panel__mark {
    position: absolute;
    left: 50%;
    top: 62px;
    width: 30px;
    height: 30px;
    margin-left: -15px;
    background: var(--accent-orange);
  }
  .brand-panel__range {
    position: absolute;
    left: 0;
    right: 0;
    top: 148px;
    margin: 0;
    font-family: "Josefin Sans", sans-serif;
    font-weight: 300;
    font-size: 26px;
    line-height: 1;
  }
  .brand-panel__name {
    position: absolute;
    left: 14px;
    right: 14px;
    top: 186px;
    margin: 0;
    font-family: "Josefin Sans", sans-serif;
    font-weight: 300;
    font-size: 41px;
    line-height: 1;
    letter-spacing: 0;
    white-space: nowrap;
  }
  .brand-panel__tagline {
    position: absolute;
    left: 0;
    right: 0;
    top: 332px;
    margin: 0;
    font-family: "Roboto Slab", serif;
    font-weight: 600;
    font-size: 16px;
    line-height: 1;
  }
</style>
</head>
<body>
  <main class="canvas">
    <section class="label">
      <div class="label__pattern" role="img" aria-label="Repeating geometric cube line pattern in navy on white"></div>
      <div class="brand-panel">
        <div class="brand-panel__frame"></div>
        <div class="brand-panel__mark"></div>
        <p class="brand-panel__range">Skin Repair</p>
        <h1 class="brand-panel__name">KOLA EMU</h1>
        <p class="brand-panel__tagline">Probiotic Skin Care</p>
      </div>
    </section>
  </main>
</body>
</html>
```